Bright Path Crest Home Realty yard sign Logo

UPDATE Design logo for Realty yard sign. 24x24 diamond or 36x24 Rectangle.
Open to all ideas. We are a discount firm but want to project a high end feel. We provide 100% of all services and extensive marketing for 1/2 the fee.
The following info must be on sign
BRIGHT PATH CREST (OR 1/3) HOME REALTY
Dennis Morrow 492-7306
CresthomeQV.com

Target Market(s)

home sellers and buyers

Industry/Entity Type

Real Estate yard sign please see sign attached in gif

Logo Text

Bright Path Crest Home Realty OR (1/3 IN PLACE OF CREST)

Requirements
Must have
• BRIGHT PATH CREST (OR 1/3) HOME REALTY Dennis Morrow 492-7306 CresthomeQV.com FOR SALE (optional)

```html
<!DOCTYPE html>
<html lang="en">
<head>
<meta charset="utf-8">
<title>Bright Path Crest Home Realty – Yard Sign</title>
<link rel="stylesheet" href="https://fonts.googleapis.com/css2?family=Montserrat:ital,wght@0,500;0,700;0,800;1,700&display=swap">
<style>
  :root {
    --brand-blue: #344f86;
    --brand-green: #8ebb3c;
    --sign-face: #e8e6e7;
    --page: #ffffff;
    --text-light: #ffffff;
  }
  html, body {
    margin: 0;
    padding: 0;
    width: 1200px;
    height: 1200px;
    overflow: hidden;
    background: var(--page);
  }
  .yard-sign {
    display: block;
    width: 1200px;
    height: 1200px;
  }
  .sign-face { fill: var(--sign-face); }
  .for-sale-cap { fill: var(--brand-blue); }
  .for-sale-label {
    fill: var(--text-light);
    font-family: "Montserrat", sans-serif;
    font-weight: 800;
    font-size: 46px;
    letter-spacing: 1px;
  }
  .tagline,
  .fraction {
    fill: var(--brand-green);
    font-family: "Montserrat", sans-serif;
    font-weight: 800;
    font-size: 94px;
  }
  .brand-name {
    fill: var(--brand-blue);
    font-family: "Montserrat", sans-serif;
    font-weight: 800;
    font-size: 108px;
  }
  .brand-dot { fill: var(--brand-green); }
  .agent-name {
    fill: var(--brand-blue);
    font-family: "Montserrat", sans-serif;
    font-weight: 700;
    font-size: 58px;
  }
  .agent-phone {
    fill: var(--brand-green);
    font-family: "Montserrat", sans-serif;
    font-style: italic;
    font-weight: 700;
    font-size: 78px;
  }
  .agent-web {
    fill: var(--brand-blue);
    font-family: "Montserrat", sans-serif;
    font-weight: 500;
    font-size: 44px;
  }
</style>
</head>
<body>
<svg class="yard-sign" viewBox="0 0 1200 1200" xmlns="http://www.w3.org/2000/svg" role="img" aria-label="For sale yard sign for Bright Path Crest Home Realty, Dennis Morrow, 492-7306, CresthomeQV.com">
  <polygon class="sign-face" points="600,120 1080,600 600,1080 120,600"/>
  <polygon class="for-sale-cap" points="600,120 777,297 423,297"/>
  <text class="for-sale-label" x="600" y="280" text-anchor="middle">FOR SALE</text>

  <text class="tagline" x="600" y="398" text-anchor="middle" textLength="360" lengthAdjust="spacingAndGlyphs">BRIGHT</text>
  <text class="tagline" x="420" y="490" textLength="218" lengthAdjust="spacingAndGlyphs">PATH</text>
  <text class="fraction" x="668" y="490" textLength="150" lengthAdjust="spacingAndGlyphs">1/3</text>

  <text class="brand-name" x="600" y="628" text-anchor="middle" textLength="680" lengthAdjust="spacingAndGlyphs">Home Realty</text>

  <circle class="brand-dot" cx="375" cy="715" r="52"/>
  <text class="agent-name" x="455" y="736" textLength="420" lengthAdjust="spacingAndGlyphs">Dennis Morrow</text>

  <text class="agent-phone" x="600" y="833" text-anchor="middle" textLength="300" lengthAdjust="spacingAndGlyphs">492-7306</text>
  <text class="agent-web" x="600" y="890" text-anchor="middle" textLength="300" lengthAdjust="spacingAndGlyphs">CresthomeQV.com</text>
</svg>
</body>
</html>
```